Corporate Design für eine Hautarztpraxis gesucht
Die Zusammenarbeit mit TELUVI war geprägt von höchster Professionalität. Als erstes natürlich das Ergebnis, die Aussagekraft und die Anmutung des entworfenen Designs, da wurden die Anforderungen zu 100 % umgesetzt. Top-Kreativer mit Einfühlungsvermögen in den Kundenwunsch. Als zweites die Zusammenarbeit; verbindliche Kommunikation, die Designentwürfe wurden von TELUVI erklärt und er scheut nicht davor zurück, mitzuteilen wenn die Änderungswünsche vom Briefing und seiner Vorstellung der Umsetzung abweichen, prompte Reaktion auf Kommentare Als drittes die Zuverlässigkeit; alle Zusagen wurden eingehalten, auch das Feintuning nach Projektende war vorbildlich. Zusammenfassend: Top Designer, Vollprofi und 100% Zufriedenheit, danke und jederzeit gerne wieder!!! Working with TELUVI in the project was highly professional. First of all the result and the appearance of the logo and the printproducts; the job fullfillment has reached 100%. TELUVI is a top-creative with understanding and feeling for customer needs. Secondly working with him; the drafts were explained, communication to the point and fast responses to the remarks, and he was free in telling his opinion, if the remarks would lead in the wrong direction Third the reliability; everything was delivered, nothing missed, also the work and finetuning after the official end of the project was to our full satisfaction. Conclusion: Top designer, a real pro, 100 % satisfaction, thanks a lot and we would do it always again!!!
Zielgruppe
Neugründung einer Hautarztpraxis (Gemeinschaftspraxis) von drei Ärzten/Innen
Angeboten wird ein umfassendes medizinisches Spektrum für Kassen- und Privatpatienten sowie Dienstleistungen im Bereich Dermatologischer Kosmetik (Anti Aging, Lasertherapie, Botox, ...)
Die Zielgruppe besteht also zum einen Teil aus Patienten mit gesundheitlichen Problemen der Haut und Allergien sowie andererseits aus Kunden die kosmetische Dienstleistungen nachfragen.
Aufgabenstellung
In Bezug auf die Gestaltung sind wir sehr offen und haben noch keine konkrete Vorstellung, freuen uns aber über viele kreative Vorschläge, von denen wir uns den initialen Impuls für das Design des zukünftigen Logos erhoffen, welches dann im Projekt entwickelt werden soll.
Das Logo soll auf jeden Fall aus einer Wort- und Bildmarke bestehen (Prio 1), eventuell in ein Wappen/Emblem eingebunden sein (Prio 2).
Die Haut als menschliches Organ hat vielschichtige Funktionen, sie schützt den Organismus vor äußeren Umwelteinflüssen und repräsentiert den Menschen nach außen.
Die Haut steht auch für Sensibilität, Reinheit und Schönheit, diese Attribute könnten sich im Logo wiederfinden.
Das Logo soll Kompetenz, Seriosität, Eleganz und Sympathie ausstrahlen, dem Kunden Vertrauen vermitteln und im Verhältnis zur Wortmarke gleich stark sein, so dass z.B. bei der Visitenkarte und dem Briefpapier die Anordnung der Wort- zur Bildmarke unterschiedlich gestaltet werden kann.
Feedback können wir erst in den Abendstunden geben, da tagsüber gearbeitet werden muss und das aktuell noch in unterschiedlichen Arztpraxen.

```html
<!DOCTYPE html>
<html lang="de">
<head>
<meta charset="utf-8">
<title>Hautpraxis Lindenau – Geschäftsausstattung</title>
<link href="https://fonts.googleapis.com/css2?family=Josefin+Sans:wght@300;400&display=swap" rel="stylesheet">
<style>
  :root {
    --bg: #f3f3f3;
    --paper: #ffffff;
    --ink: #5f5f5f;
    --ink-soft: #8a8a8a;
    --rose: #ef8d9c;
    --slate: #6f6f6f;
    --window: #a9a9a9;
    --label: #6a6a6a;
  }
  * { margin: 0; padding: 0; box-sizing: border-box; }
  html, body { width: 1200px; height: 801px; overflow: hidden; }
  body {
    background: radial-gradient(ellipse at 40% 40%, #ffffff 0%, var(--bg) 70%, #e9e9e9 100%);
    font-family: "Josefin Sans", sans-serif;
    font-weight: 300;
    color: var(--ink);
    position: relative;
  }
  .wordmark {
    position: absolute;
    display: flex;
    align-items: center;
    gap: 0.35em;
    color: var(--ink);
    font-weight: 300;
    white-space: nowrap;
    line-height: 1;
  }
  .wordmark .dot {
    width: 0.45em; height: 0.45em;
    border-radius: 50%;
    background: var(--rose);
    flex: none;
  }
  .hero-mark { left: 180px; top: 118px; font-size: 42px; }

  .label {
    position: absolute;
    font-size: 14px;
    color: var(--label);
    text-align: center;
    width: 260px;
  }
  .sheet {
    position: absolute;
    background: var(--paper);
    box-shadow: 3px 4px 8px rgba(0,0,0,0.28);
    overflow: hidden;
  }
  .card-front { left: 58px; top: 293px; width: 260px; height: 166px; }
  .card-front .wordmark { left: 42px; top: 72px; font-size: 19px; }

  .card-back { left: 335px; top: 293px; width: 258px; height: 166px; }
  .card-back svg.band { position: absolute; inset: 0; }
  .card-back .wordmark { left: 12px; top: 26px; font-size: 11px; }
  .card-back .details {
    position: absolute; right: 18px; top: 24px;
    text-align: right; color: #fff; font-size: 10.5px; line-height: 1.35;
  }
  .card-back .details .name { margin-bottom: 36px; }

  .envelope { left: 58px; top: 505px; width: 536px; height: 265px; }
  .envelope .wordmark { left: 48px; top: 48px; font-size: 18px; }
  .envelope .window {
    position: absolute; left: 47px; top: 120px; width: 203px; height: 110px;
    border-radius: 10px;
    background: linear-gradient(135deg, #b9b9b9, var(--window));
  }

  .fold { position: absolute; left: 621px; width: 12px; height: 1px; background: var(--ink); }
  .fold.punch { background: var(--rose); }

  .letter { left: 631px; top: 34px; width: 520px; height: 736px; font-size: 6px; }
  .letter svg.band { position: absolute; inset: 0; }
  .letter .wordmark { right: 30px; top: 40px; font-size: 16px; }
  .letter .sender { position: absolute; left: 59px; top: 111px; font-size: 5px; color: var(--ink-soft); }
  .letter .recipient { position: absolute; left: 59px; top: 152px; font-size: 6.5px; line-height: 1.55; }
  .letter .contact {
    position: absolute; right: 30px; top: 122px;
    text-align: right; color: var(--rose); font-size: 5.8px; line-height: 1.7;
  }
  .letter .contact .gap { margin-top: 8px; }
  .letter .body { position: absolute; left: 59px; top: 233px; width: 370px; font-size: 6.3px; line-height: 1.5; }
  .letter .body p { margin-bottom: 8px; }
  .letter .body .subject { margin-bottom: 18px; }
  .letter .footer {
    position: absolute; top: 669px; font-size: 5.8px; line-height: 1.75; color: var(--rose);
  }
  .letter .footer.bank { color: #fff; }
</style>
</head>
<body>

  <div class="wordmark hero-mark"><span>Hautpraxis Lindenau</span><span class="dot"></span></div>

  <div class="label" style="left:58px; top:263px;">Visitenkarte vorne</div>
  <div class="label" style="left:334px; top:263px;">Visitenkarte hinten</div>

  <section class="sheet card-front">
    <div class="wordmark"><span>Hautpraxis Lindenau</span></div>
  </section>

  <section class="sheet card-back">
    <svg class="band" width="258" height="166" viewBox="0 0 258 166" aria-hidden="true">
      <polygon points="150,0 258,0 258,166 0,166 0,160" fill="var(--slate)"/>
    </svg>
    <div class="wordmark"><span>Hautpraxis Lindenau</span></div>
    <div class="details">
      <div class="name">Dr. med.<br>Max<br>Mustermann</div>
      <div>Musterstraße 2<br>12345 Berlin<br>Tel.: 0123 45 67 89<br>info@hautpraxis-lindenau.de</div>
    </div>
  </section>

  <section class="sheet envelope">
    <div class="wordmark"><span>Hautpraxis Lindenau</span></div>
    <div class="window"></div>
  </section>

  <div class="fold" style="top:290px;"></div>
  <div class="fold punch" style="top:397px;"></div>
  <div class="fold" style="top:546px;"></div>

  <section class="sheet letter">
    <svg class="band" width="520" height="736" viewBox="0 0 520 736" aria-hidden="true">
      <polygon points="520,497 520,736 284,736" fill="var(--slate)"/>
    </svg>
    <div class="wordmark"><span>Hautpraxis Lindenau</span></div>
    <div class="sender">hautpraxis-lindenau.de | Musterstraße 2 | 12345 Berlin</div>
    <div class="recipient">Herr Mustermann<br>Musterstraße 3<br>48555 Muster</div>
    <div class="contact">
      hautpraxis-lindenau.de<br>Musterstr. 2<br>12345 Berlin<br>Tel.: 0123 45 67 89<br>Fax: 0123 45 67 8<br>Mobil: 0173 4567890
      <div class="gap">info@hautpraxis-lindenau.de<br>www.hautpraxis-lindenau.de</div>
    </div>
    <div class="body">
      <p class="subject">Hier steht eine Betreffzeile</p>
      <p>Sehr geehrte Frau Musterbeispiel,</p>
      <p>als Kunde unseres jungen und modernen Unternehmens erwartet<br>Sie Qualität in höchstem Maße.</p>
      <p>Sie können sicher zu sein, genau zu bekommen, was wir Ihnen versprechen.<br>Und damit werden Sie auch rundum zufrieden sein. Das garantieren wir Ihnen.</p>
      <p>Schauen Sie doch gleich das beiliegende Prospekt. Wir bieten Ihnen moderne und hochwertige Produkte, die auf dem neuesten Stand der Technik sind, an. Überzeugen Sie sich selbst von der hochwertigen Qualität unserer Produkte und bestellen Sie noch heute.</p>
      <p>Wir freuen uns auf Ihre Bestellung und sind bei Rückfragen gerne für Sie da.</p>
      <p style="margin-top:18px;">Mit freundlichen Grüßen</p>
    </div>
    <div class="footer" style="left:59px;">hautpraxis-lindenau.de<br>Musterstraße 2<br>12345 Berlin</div>
    <div class="footer" style="left:199px;">USt-IDNR.: DE123467<br>Steuernummer: 12345/67/89<br>Inhaber: Max Mustermann</div>
    <div class="footer bank" style="left:349px;">Stadtbank Musterstadt<br>IBAN: DE05 1555 0000 0000 1111<br>BIC: WELNAXXX77</div>
  </section>

</body>
</html>
```